Meadowlark Counseling Partners, LLC Needs Modern Business Card Design.

We provide behavioral health services from western Kansas to eastern Kansas. There is an abundance of competition for the services we provide with our main competitor being larger and having significantly more financial resources; however, the quality of services we provide is greater and we have started to catch the attention of the State of Kansas. We had a great logo designed by ArtFolio - this will be used to build upon our brand. The logo (attached) should be used in the card development. We want something unique, modern, but also a card design that clearly states our name, contact info, provides the name and unqiue location of each clinician, etc. Rounded edges, or a unique size, just something that makes our business card stand out from others. I have also uploaded each clinician's name and their unique location and phone number.

Our idea is to have one side be black with our logo. Then, on the other side have business cards for each individual. Plus, we want one card that is "generic" with no specific clinician's name listed so that we can give clients an appointment card when they leave. Some clinicians have two locations - we're open to design and background color, but we have started going with branding colors of black, the yellow in the logo files attached, and sometimes a gray. Our new office has been decorated using this theme.

Target Market(s)

individuals and families in need of behavioral health services; potential professional referral sources; existing referral sources

Industry/Entity Type

Business

Contact Information for Business Card

I attached a Word doc that provides clinician names, credentials and location information specific to each individual.

Font styles to use
Serif

Colors
000000
fbed22
dbdbdb
9d9d9d
c3c3c3

Requirements
Must have
• 1) use of the company logo that has been attached; 2) a template that provides us space to individualize business cards for all of our clinicians; 3) should stick to the colors we are branding with: black, yellow from the logo file, maybe a gray shade and we're open to a suggestion on a shade of white.
Nice to have
• Group discussion culminated in the thought that one side would be black with just our logo - no clinician names, etc. A unique design - rounded edges, unique size, some catchy lay-out would be nice.
Should not have
• Must not be too busy. Should look "clean." The project should stick to branding colors: black, yellow (from the logo file), maybe a gray and shade of white.

```html
<!DOCTYPE html>
<html lang="en">
<head>
<meta charset="utf-8">
<title>Meadowlark Counseling Partners, LLC – Business Card</title>
<link href="https://fonts.googleapis.com/css2?family=EB+Garamond:wght@400;500;600&display=swap" rel="stylesheet">
<style>
  :root {
    --bg: #e4e5e6;
    --black: #000000;
    --yellow: #fbed22;
    --gold: #f2c21b;
    --pale-gold: #f7df8a;
    --white: #ffffff;
    --gray-light: #dbdbdb;
    --gray-mid: #c3c3c3;
    --gray: #9d9d9d;
    --ink: #1a1a1a;
    --icon: #8a8a8a;
  }
  * { box-sizing: border-box; margin: 0; padding: 0; }
  html, body {
    width: 1200px; height: 717px; overflow: hidden;
    background: var(--bg);
    font-family: "EB Garamond", Georgia, serif;
  }
  .sheet {
    width: 1200px; height: 717px;
    display: flex; align-items: center; justify-content: center; gap: 60px;
  }
  .card {
    width: 520px; height: 298px;
    border-radius: 26px;
    position: relative;
    box-shadow: 0 6px 18px rgba(0,0,0,0.12);
  }
  .card--front {
    background: var(--black);
    display: flex; align-items: center; justify-content: center;
  }
  .brand {
    display: flex; align-items: center; gap: 12px;
  }
  .brand__dot {
    width: 22px; height: 22px; border-radius: 50%;
    background: var(--gold);
  }
  .brand__name {
    color: var(--gold);
    font-size: 24px; font-weight: 500;
    letter-spacing: 0.04em;
  }
  .card--back {
    background: var(--white);
    color: var(--ink);
  }
  .back__brand {
    position: absolute; top: 34px; left: 0; right: 0;
    text-align: center;
    color: var(--pale-gold);
    font-size: 15px; font-weight: 500; letter-spacing: 0.06em;
  }
  .holder {
    position: absolute; left: 40px; top: 112px;
  }
  .holder__name {
    font-size: 27px; font-weight: 500; line-height: 1.05;
    white-space: nowrap;
  }
  .holder__title {
    font-size: 21px; color: var(--gray); line-height: 1.1;
  }
  .location {
    position: absolute;
    font-size: 14.5px; line-height: 1.2;
    white-space: nowrap;
  }
  .location--primary { left: 40px; top: 196px; }
  .location--secondary { left: 320px; top: 112px; }
  .line {
    display: flex; align-items: flex-start; gap: 10px; margin-bottom: 6px;
  }
  .line svg { flex: none; margin-top: 2px; fill: var(--icon); }
</style>
</head>
<body>
<main class="sheet">
  <section class="card card--front" aria-label="Card front">
    <div class="brand">
      <span class="brand__dot"></span>
      <span class="brand__name">Meadowlark Counseling Partners, LLC</span>
    </div>
  </section>

  <section class="card card--back" aria-label="Card back">
    <div class="back__brand">Meadowlark Counseling Partners, LLC</div>

    <div class="holder">
      <div class="holder__name">Daniel R. Hartwell, LP</div>
      <div class="holder__title">President</div>
    </div>

    <div class="location location--primary">
      <div class="line">
        <svg width="11" height="14" viewBox="0 0 11 14" aria-hidden="true"><path d="M5.5 0A5.5 5.5 0 0 0 0 5.5C0 9.5 5.5 14 5.5 14S11 9.5 11 5.5A5.5 5.5 0 0 0 5.5 0zm0 7.6a2.1 2.1 0 1 1 0-4.2 2.1 2.1 0 0 1 0 4.2z"/></svg>
        <span>418 N. Elm Row<br>Prairie Glen, Kansas 60412</span>
      </div>
      <div class="line">
        <svg width="12" height="12" viewBox="0 0 24 24" aria-hidden="true"><path d="M6.6 10.8a15.2 15.2 0 0 0 6.6 6.6l2.2-2.2a1 1 0 0 1 1-.25 11.4 11.4 0 0 0 3.6.57 1 1 0 0 1 1 1V20a1 1 0 0 1-1 1A17 17 0 0 1 3 4a1 1 0 0 1 1-1h3.5a1 1 0 0 1 1 1c0 1.25.2 2.45.57 3.57a1 1 0 0 1-.25 1z"/></svg>
        <span>(555) 014-2236</span>
      </div>
    </div>

    <div class="location location--secondary">
      <div class="line">
        <svg width="11" height="14" viewBox="0 0 11 14" aria-hidden="true"><path d="M5.5 0A5.5 5.5 0 0 0 0 5.5C0 9.5 5.5 14 5.5 14S11 9.5 11 5.5A5.5 5.5 0 0 0 5.5 0zm0 7.6a2.1 2.1 0 1 1 0-4.2 2.1 2.1 0 0 1 0 4.2z"/></svg>
        <span>205 W. Cedar Ave., Ste. 110<br>Willow Bend, Kansas 60738</span>
      </div>
      <div class="line">
        <svg width="12" height="12" viewBox="0 0 24 24" aria-hidden="true"><path d="M6.6 10.8a15.2 15.2 0 0 0 6.6 6.6l2.2-2.2a1 1 0 0 1 1-.25 11.4 11.4 0 0 0 3.6.57 1 1 0 0 1 1 1V20a1 1 0 0 1-1 1A17 17 0 0 1 3 4a1 1 0 0 1 1-1h3.5a1 1 0 0 1 1 1c0 1.25.2 2.45.57 3.57a1 1 0 0 1-.25 1z"/></svg>
        <span>(555) 019-0040</span>
      </div>
    </div>
  </section>
</main>
</body>
</html>
```